Stationery Design
Letterhead, Envelope, Business Card, Email signature design
I need single sided standard sized Business Card [3.5" x 2"]
Myriad Pro
Professional
Corisse Pallant
Brand Manager
4127 Dunford Avenue
Burnaby, B.C. V3K 8T2
604-281-7734 ext. 120
corisse@brightfernco.ca
brightfernco.ca
We are a family-owned school photography company in Western Canada. We've just had a new logo and website designed and need some new stationery.
This is the .ai file we would like to use for the stationery design. Please refer to our website, brightfernco.ca, for more information about our brand.

```html
<!DOCTYPE html>
<html lang="en">
<head>
<meta charset="utf-8">
<title>Bright Fern Co. — Stationery</title>
<link href="https://fonts.googleapis.com/css2?family=Source+Sans+3:wght@400;600;700&display=swap" rel="stylesheet">
<style>
  :root{
    --bg-dark:#2e3032;
    --bg-mid:#45484b;
    --teal:#27a3c4;
    --teal-dark:#1b7f9a;
    --paper:#ffffff;
    --ink:#3b3f43;
    --ink-soft:#8a9096;
    --ghost:#e6eef2;
  }
  *{box-sizing:border-box;margin:0;padding:0}
  html,body{width:1200px;height:314px;overflow:hidden}
  body{
    position:relative;
    background:radial-gradient(ellipse at 55% 45%,var(--bg-mid),var(--bg-dark));
    font-family:"Source Sans 3",sans-serif;color:var(--ink);
  }
  .piece{position:absolute;background:var(--paper);box-shadow:0 2px 6px rgba(0,0,0,.45)}
  .brand{display:flex;align-items:center;gap:4px}
  .brand__mark{background:var(--teal);flex:none}
  .brand__name{font-weight:700;color:var(--ink);letter-spacing:.04em;white-space:nowrap;line-height:1}

  /* hero logo */
  .hero{position:absolute;left:12px;top:22px}
  .hero .brand__mark{width:26px;height:26px}
  .hero .brand__name{font-size:21px;color:var(--paper)}
  .hero__tagline{margin:6px 0 0 30px;font-size:8px;color:#b9c2c7;letter-spacing:.05em}

  /* business cards */
  .card{width:122px;height:68px;padding:8px}
  .card--front{left:67px;top:126px}
  .card--front .brand__mark{width:9px;height:9px}
  .card--front .brand__name{font-size:8px}
  .card__details{margin-top:8px;font-size:4.5px;line-height:1.45;color:var(--ink)}
  .card__details strong{font-size:5.5px;font-weight:600}
  .card--plain{left:12px;top:216px;width:121px;height:67px}
  .card--plain::after{content:"";position:absolute;left:0;right:0;bottom:10px;height:3px;background:var(--teal)}
  .card--teal{left:139px;top:216px;width:125px;height:67px;background:var(--teal);display:flex;align-items:center;justify-content:center}
  .card--teal .brand__mark{width:10px;height:10px;background:var(--paper)}
  .card--teal .brand__name{font-size:9px;color:var(--paper)}

  /* letterheads */
  .letterhead{top:12px;width:197px;height:271px;border-left:4px solid var(--teal);padding:10px 12px}
  .letterhead--a{left:283px}
  .letterhead--b{left:494px}
  .letterhead__head{display:flex;justify-content:space-between;align-items:flex-start}
  .letterhead .brand__mark{width:8px;height:8px}
  .letterhead .brand__name{font-size:7px}
  .letterhead__contact{font-size:3.6px;line-height:1.5;text-align:right;color:var(--ink-soft)}
  .letterhead__ghost{position:absolute;left:70px;top:100px;width:52px;height:52px;background:var(--ghost)}

  /* email signatures */
  .signature{width:221px;border-left:3px solid var(--teal);padding:7px 8px}
  .signature--strip{left:727px;top:24px;width:150px;height:24px;padding:5px 7px;border-left:none;border-bottom:3px solid var(--teal)}
  .signature--strip .brand__mark{width:8px;height:8px}
  .signature--strip .brand__name{font-size:7px}
  .signature--one{left:703px;top:72px;height:103px}
  .signature--two{left:703px;top:185px;height:110px}
  .signature .brand__mark{width:8px;height:8px}
  .signature .brand__name{font-size:7px}
  .signature__details{margin-top:6px;font-size:4px;line-height:1.5;color:var(--ink-soft)}
  .signature__ghost{position:absolute;right:40px;bottom:18px;width:40px;height:40px;background:var(--ghost)}

  /* envelopes */
  .envelope{left:943px;width:233px}
  .envelope--teal{top:122px;height:76px}
  .envelope--white{top:204px;height:89px}
  .envelope svg{position:absolute;inset:0}
  .envelope .brand{position:absolute;left:50%;transform:translateX(-50%)}
  .envelope .brand__mark{width:7px;height:7px}
  .envelope .brand__name{font-size:6px}
  .envelope--teal .brand{top:34px}
  .envelope--white .brand{top:46px}
  .envelope--teal .brand__mark{background:var(--paper)}
  .envelope--teal .brand__name{color:var(--paper)}
</style>
</head>
<body>

<header class="hero">
  <div class="brand"><span class="brand__mark"></span><span class="brand__name">BRIGHT FERN CO.</span></div>
  <p class="hero__tagline">Capturing school memories</p>
</header>

<section class="piece card card--front">
  <div class="brand"><span class="brand__mark"></span><span class="brand__name">BRIGHT FERN CO.</span></div>
  <p class="card__details">
    <strong>Corisse Pallant</strong><br>Brand Manager<br>
    4127 Dunford Avenue<br>Burnaby, B.C. V3K 8T2<br>
    604-281-7734 ext. 120<br>corisse@brightfernco.ca<br>brightfernco.ca
  </p>
</section>
<section class="piece card card--plain"></section>
<section class="piece card card--teal">
  <div class="brand"><span class="brand__mark"></span><span class="brand__name">BRIGHT FERN CO.</span></div>
</section>

<section class="piece letterhead letterhead--a">
  <div class="letterhead__head">
    <div class="brand"><span class="brand__mark"></span><span class="brand__name">BRIGHT FERN CO.</span></div>
    <p class="letterhead__contact">4127 Dunford Avenue<br>Burnaby, B.C. V3K 8T2<br>604-281-7734 ext. 120<br>brightfernco.ca</p>
  </div>
  <div class="letterhead__ghost"></div>
</section>
<section class="piece letterhead letterhead--b">
  <div class="letterhead__head">
    <div class="brand"><span class="brand__mark"></span><span class="brand__name">BRIGHT FERN CO.</span></div>
  </div>
  <div class="letterhead__ghost"></div>
</section>

<section class="piece signature signature--strip">
  <div class="brand"><span class="brand__mark"></span><span class="brand__name">BRIGHT FERN CO.</span></div>
</section>
<section class="piece signature signature--one">
  <div class="brand"><span class="brand__mark"></span><span class="brand__name">BRIGHT FERN CO.</span></div>
  <p class="signature__details">Corisse Pallant · Brand Manager<br>604-281-7734 ext. 120<br>corisse@brightfernco.ca</p>
  <div class="signature__ghost"></div>
</section>
<section class="piece signature signature--two">
  <div class="brand"><span class="brand__mark"></span><span class="brand__name">BRIGHT FERN CO.</span></div>
  <p class="signature__details">Corisse Pallant · Brand Manager<br>604-281-7734 ext. 120<br>brightfernco.ca</p>
  <div class="signature__ghost"></div>
</section>

<section class="piece envelope envelope--teal">
  <svg viewBox="0 0 233 76" preserveAspectRatio="none">
    <polygon points="0,0 233,0 116.5,62" fill="var(--teal)"/>
  </svg>
  <div class="brand"><span class="brand__mark"></span><span class="brand__name">BRIGHT FERN CO.</span></div>
</section>
<section class="piece envelope envelope--white">
  <svg viewBox="0 0 233 89" preserveAspectRatio="none">
    <polyline points="0,0 116.5,40 233,0" fill="none" stroke="#c9d3d8" stroke-width="1"/>
    <polyline points="0,89 116.5,50 233,89" fill="none" stroke="#c9d3d8" stroke-width="1"/>
  </svg>
  <div class="brand"><span class="brand__mark"></span><span class="brand__name">BRIGHT FERN CO.</span></div>
</section>

</body>
</html>
```